Business Card Design Project

2 sided business card utilizing existing logo
- English on one side, Arabic on the other side (both English and Arabic text will be provided)
Same color scheme as logo
Information included will be: name, title, email, phone, address and website (www.veralunix.com)
Updates

Target Market(s)

We are a Systems Integration Company

Industry/Entity Type

Business

Font styles to use
Serif
Sans Serif

Requirements
Should not have
• We prefer using the flat logo rather than one with shadow/3D effect

```html
<!DOCTYPE html>
<html lang="en">
<head>
<meta charset="utf-8">
<title>Veralunix business cards</title>
<link href="https://fonts.googleapis.com/css2?family=Arimo:wght@400;700&family=Noto+Naskh+Arabic:wght@400;700&display=swap" rel="stylesheet">
<style>
  :root {
    --canvas: #b3b3b3;
    --red: #e30613;
    --red-deep: #c10008;
    --pink: #fcd6d6;
    --white: #ffffff;
    --latin: "Arimo", Arial, sans-serif;
    --arabic: "Noto Naskh Arabic", "Arimo", serif;
  }
  * { margin: 0; padding: 0; box-sizing: border-box; }
  html, body { width: 824px; height: 1200px; overflow: hidden; }
  body { background: var(--canvas); font-family: var(--latin); }
  .sheet { position: relative; width: 824px; height: 1200px; }

  .card {
    position: absolute; width: 359px; height: 199px; overflow: hidden;
    background: var(--white); color: var(--red);
    box-shadow: 0 1px 3px rgba(0,0,0,.25);
  }
  .card--red { background: radial-gradient(circle at 45% 40%, #f0141c 0%, var(--red) 45%, var(--red-deep) 100%); color: var(--white); }
  .card--rounded { border-radius: 10px; }

  .col-en { left: 41px; } .col-ar { left: 427px; }
  .row-1 { top: 27px; } .row-2 { top: 265px; } .row-3 { top: 509px; }
  .row-4 { top: 738px; } .row-5 { top: 971px; }

  .deco { position: absolute; inset: 0; width: 359px; height: 199px; }

  .owner { position: absolute; top: 12px; right: 16px; text-align: right; }
  .owner-name { font-size: 10.5px; font-weight: 700; line-height: 1.1; }
  .owner-role { font-size: 6.5px; line-height: 1.3; color: inherit; }
  [lang="ar"] .owner-name { font-family: var(--arabic); font-size: 14px; line-height: 1.2; }
  [lang="ar"] .owner-role { font-family: var(--arabic); font-size: 8px; line-height: 1; }
  .card--white .owner-role { color: #555; }
  .card--white[lang="ar"] .owner-role { color: var(--red); }

  .brand {
    position: absolute; display: flex; align-items: center; justify-content: center; gap: 7px;
  }
  .brand--center { left: 0; right: 0; top: 74px; }
  .brand--left { left: 20px; width: 160px; top: 82px; }
  .brand--panel { left: 0; width: 147px; top: 76px; }
  .brand-square { width: 11px; height: 11px; background: currentColor; }
  .brand-name { font-family: var(--latin); font-weight: 700; font-size: 17px; letter-spacing: 4px; }
  .brand--panel .brand-name { font-size: 14px; letter-spacing: 3px; }

  .rule { position: absolute; left: 30px; right: 14px; top: 146px; height: 1px; background: currentColor; }
  .rule--wide { left: 25px; right: 14px; }
  .rule--footer { left: 28px; right: 28px; top: 175px; }

  .contact { position: absolute; list-style: none; font-size: 5.6px; line-height: 10px; }
  .contact li { white-space: nowrap; }
  .contact b { display: inline-block; width: 26px; font-weight: 400; }
  .contact--main { left: 33px; top: 153px; }
  .contact--side { left: 180px; top: 116px; }
  [lang="ar"] .contact { direction: rtl; text-align: right; font-family: var(--arabic); font-size: 5.6px; }
  [lang="ar"] .contact--main { left: 28px; width: 150px; }
  [lang="ar"] .contact--side { left: 196px; width: 140px; }
  [lang="ar"] .contact b { width: auto; margin-left: 4px; }
  .contact-line {
    position: absolute; left: 0; right: 0; top: 181px; text-align: center; font-size: 5.6px;
  }
  [lang="ar"] .contact-line { font-family: var(--arabic); direction: rtl; }

  .web { position: absolute; right: 20px; bottom: 5px; font-size: 8px; letter-spacing: 1.4px; }
  .web--on-band { color: var(--white); }
  .card--red .web { color: var(--red); }
  .web--under { left: 0; right: 0; text-align: center; top: 108px; bottom: auto; }
  .web--panel { left: 0; width: 147px; right: auto; top: 99px; bottom: auto; text-align: center; font-size: 6.5px; color: var(--white); }

  .panel { position: absolute; left: 0; top: 0; width: 147px; height: 199px; background: var(--red); color: var(--white); }
  .side-owner { position: absolute; left: 187px; top: 78px; text-align: left; }
  [lang="ar"] .side-owner { left: 206px; top: 68px; text-align: right; }
</style>
</head>
<body>
<main class="sheet">

  <!-- Design 1: red front -->
  <article class="card card--red col-en row-1" lang="en">
    <svg class="deco" viewBox="0 0 359 199" aria-hidden="true">
      <polygon points="95,0 135,0 0,135 0,95" fill="#ffffff" opacity=".12"/>
      <polygon points="205,179 359,179 359,199 183,199" fill="#ffffff"/>
    </svg>
    <div class="owner"><p class="owner-name">Name of owner</p><p class="owner-role">Designation</p></div>
    <div class="brand brand--center"><span class="brand-square"></span><span class="brand-name">VERALUNIX</span></div>
    <div class="rule"></div>
    <ul class="contact contact--main">
      <li><b>Address</b>:48 Harlow Ave. Suite 12, Fenwick, NY 10231</li>
      <li><b>Phone</b>:555-014-2288</li>
      <li><b>Email</b>:sample@veralunix.com</li>
    </ul>
    <p class="web">www.veralunix.com</p>
  </article>
  <article class="card card--red col-ar row-1" lang="ar">
    <svg class="deco" viewBox="0 0 359 199" aria-hidden="true">
      <polygon points="95,0 135,0 0,135 0,95" fill="#ffffff" opacity=".12"/>
      <polygon points="205,179 359,179 359,199 183,199" fill="#ffffff"/>
    </svg>
    <div class="owner"><p class="owner-name">اسم المالك</p><p class="owner-role">تعيين</p></div>
    <div class="brand brand--center"><span class="brand-square"></span><span class="brand-name">VERALUNIX</span></div>
    <div class="rule"></div>
    <ul class="contact contact--main">
      <li><b>عنوان :</b>48 شارع هارلو، جناح 12، فينويك</li>
      <li><b>هاتف :</b>555-014-2288</li>
      <li><b>البريد الإلكتروني :</b>sample@veralunix.com</li>
    </ul>
    <p class="web">www.veralunix.com</p>
  </article>

  <!-- Design 2: white with red band -->
  <article class="card card--white col-en row-2" lang="en">
    <svg class="deco" viewBox="0 0 359 199" aria-hidden="true">
      <polygon points="95,0 135,0 0,135 0,95" fill="var(--pink)" opacity=".8"/>
      <polygon points="205,179 359,179 359,199 183,199" fill="var(--red)"/>
    </svg>
    <div class="owner"><p class="owner-name">Name of owner</p><p class="owner-role">Designation</p></div>
    <div class="brand brand--center"><span class="brand-square"></span><span class="brand-name">VERALUNIX</span></div>
    <ul class="contact contact--main">
      <li><b>Address</b>:48 Harlow Ave. Suite 12, Fenwick, NY 10231</li>
      <li><b>Phone</b>:555-014-2288</li>
      <li><b>Email</b>:sample@veralunix.com</li>
    </ul>
    <p class="web web--on-band">www.veralunix.com</p>
  </article>
  <article class="card card--white col-ar row-2" lang="ar">
    <svg class="deco" viewBox="0 0 359 199" aria-hidden="true">
      <polygon points="95,0 135,0 0,135 0,95" fill="var(--pink)" opacity=".8"/>
      <polygon points="205,179 359,179 359,199 183,199" fill="var(--red)"/>
    </svg>
    <div class="owner"><p class="owner-name">اسم المالك</p><p class="owner-role">تعيين</p></div>
    <div class="brand brand--center"><span class="brand-square"></span><span class="brand-name">VERALUNIX</span></div>
    <ul class="contact contact--main">
      <li><b>عنوان :</b>48 شارع هارلو، جناح 12، فينويك</li>
      <li><b>هاتف :</b>555-014-2288</li>
      <li><b>البريد الإلكتروني :</b>sample@veralunix.com</li>
    </ul>
    <p class="web web--on-band">www.veralunix.com</p>
  </article>

  <!-- Design 3: white, brand left -->
  <article class="card card--white col-en row-3" lang="en">
    <svg class="deco" viewBox="0 0 359 199" aria-hidden="true">
      <polygon points="238,0 278,0 359,81 359,121" fill="var(--pink)" opacity=".8"/>
    </svg>
    <div class="owner"><p class="owner-name">Name of owner</p><p class="owner-role">Designation</p></div>
    <div class="brand brand--left"><span class="brand-square"></span><span class="brand-name">VERALUNIX</span></div>
    <div class="rule rule--wide"></div>
    <ul class="contact contact--main">
      <li><b>Address</b>:48 Harlow Ave. Suite 12, Fenwick, NY 10231</li>
      <li><b>Phone</b>:555-014-2288</li>
      <li><b>Email</b>:sample@veralunix.com</li>
    </ul>
    <p class="web">www.veralunix.com</p>
  </article>
  <article class="card card--white col-ar row-3" lang="ar">
    <svg class="deco" viewBox="0 0 359 199" aria-hidden="true">
      <polygon points="238,0 278,0 359,81 359,121" fill="var(--pink)" opacity=".8"/>
    </svg>
    <div class="owner"><p class="owner-name">اسم المالك</p><p class="owner-role">تعيين</p></div>
    <div class="brand brand--left"><span class="brand-square"></span><span class="brand-name">VERALUNIX</span></div>
    <div class="rule rule--wide"></div>
    <ul class="contact contact--main">
      <li><b>عنوان :</b>48 شارع هارلو، جناح 12، فينويك</li>
      <li><b>هاتف :</b>555-014-2288</li>
      <li><b>البريد الإلكتروني :</b>sample@veralunix.com</li>
    </ul>
    <p class="web">www.veralunix.com</p>
  </article>

  <!-- Design 4: rounded, single-line footer -->
  <article class="card card--white card--rounded col-en row-4" lang="en">
    <div class="owner"><p class="owner-name">Name of owner</p><p class="owner-role">Designation</p></div>
    <div class="brand brand--center"><span class="brand-square"></span><span class="brand-name">VERALUNIX</span></div>
    <p class="web web--under">www.veralunix.com</p>
    <div class="rule rule--footer"></div>
    <p class="contact-line">:48 Harlow Ave. Suite 12, Fenwick, NY 10231, 555-014-2288, sample@veralunix.com</p>
  </article>
  <article class="card card--white card--rounded col-ar row-4" lang="ar">
    <div class="owner"><p class="owner-name">اسم المالك</p><p class="owner-role">تعيين</p></div>
    <div class="brand brand--center"><span class="brand-square"></span><span class="brand-name">VERALUNIX</span></div>
    <p class="web web--under">www.veralunix.com</p>
    <div class="rule rule--footer"></div>
    <p class="contact-line">48 شارع هارلو، جناح 12، فينويك، 555-014-2288، sample@veralunix.com</p>
  </article>

  <!-- Design 5: red side panel -->
  <article class="card card--white col-en row-5" lang="en">
    <svg class="deco" viewBox="0 0 359 199" aria-hidden="true">
      <polygon points="215,0 252,0 147,105 147,68" fill="var(--pink)" opacity=".8"/>
      <polygon points="280,30 317,30 190,157 190,120" fill="var(--pink)" opacity=".6"/>
    </svg>
    <div class="panel">
      <div class="brand brand--panel"><span class="brand-square"></span><span class="brand-name">VERALUNIX</span></div>
      <p class="web web--panel">www.veralunix.com</p>
    </div>
    <div class="side-owner"><p class="owner-name">Name of owner</p><p class="owner-role" style="color:#555">Designation</p></div>
    <ul class="contact contact--side">
      <li><b>Address</b>:48 Harlow Ave. Suite 12, Fenwick, NY 10231</li>
      <li><b>Phone</b>:555-014-2288</li>
      <li><b>Email</b>:sample@veralunix.com</li>
    </ul>
  </article>
  <article class="card card--white col-ar row-5" lang="ar">
    <svg class="deco" viewBox="0 0 359 199" aria-hidden="true">
      <polygon points="215,0 252,0 147,105 147,68" fill="var(--pink)" opacity=".8"/>
      <polygon points="280,30 317,30 190,157 190,120" fill="var(--pink)" opacity=".6"/>
    </svg>
    <div class="panel">
      <div class="brand brand--panel"><span class="brand-square"></span><span class="brand-name">VERALUNIX</span></div>
      <p class="web web--panel">www.veralunix.com</p>
    </div>
    <div class="side-owner"><p class="owner-name">اسم المالك</p><p class="owner-role">تعيين</p></div>
    <ul class="contact contact--side">
      <li><b>عنوان :</b>48 شارع هارلو، جناح 12، فينويك</li>
      <li><b>هاتف :</b>555-014-2288</li>
      <li><b>البريد الإلكتروني :</b>sample@veralunix.com</li>
    </ul>
  </article>

</main>
</body>
</html>
```